Business Card and Letterhead for Vantage Psychology

We need a business card design and letterhead to use for our Psychology firm that specializes in psychoeducational assessments and individual therapy. Our motto is Purpose-Driven Assessments, Meaning-Centered Therapy.Our contact information is as follows:
Vantage Psychology
The Marwick Block - 6127-48St.
Box 2716 Halvern, NB
T2K 3M8
t 403.555.0148 (VANT)
f 403.555.0172
www.vantagepsychology-example.ca
The business card will be used for two different psychologists so I can supply names nearer to completion. We prefer clean, uncluttered looks.

Target Market(s)

Clients, Educators

Font styles to use
Sans Serif

Colors

Designer to choose colors to be used in the design.

Requirements
Must have
• All relevant contact info, logo, some "white" space.
Nice to have
• It would be nice to see letterhead options that have the logo on the top of the page but also options that have it on the side. I think top of the page is probably our preference.
Should not have
• Too much clutter!

```html
<!DOCTYPE html>
<html lang="en">
<head>
<meta charset="utf-8">
<title>Vantage Psychology – Business Card</title>
<link href="https://fonts.googleapis.com/css2?family=Roboto:wght@400;500;700;900&display=swap" rel="stylesheet">
<style>
  :root {
    --bg: #3a3a3c;
    --card: #ffffff;
    --blue: #4fb8d9;
    --orange: #f6a05a;
    --ink: #1c1c1c;
    --rule: #2a2a2a;
  }
  * { box-sizing: border-box; margin: 0; padding: 0; }
  html, body { width: 1200px; height: 1200px; overflow: hidden; }
  body {
    background: var(--bg);
    font-family: "Roboto", Arial, sans-serif;
    color: var(--ink);
    position: relative;
  }
  .card {
    position: absolute;
    left: 180px;
    width: 840px;
    height: 480px;
    background: var(--card);
    border-radius: 30px;
    overflow: hidden;
    box-shadow: 0 14px 30px rgba(0,0,0,.35);
  }
  .card--front { top: 90px; }
  .card--back { top: 630px; }

  .wordmark {
    display: flex;
    align-items: center;
    gap: 18px;
    color: var(--blue);
    font-weight: 500;
    text-transform: uppercase;
    letter-spacing: 2px;
    white-space: nowrap;
  }
  .wordmark__dot {
    border-radius: 50%;
    background: var(--blue);
    flex: none;
  }
  .card--front .wordmark {
    position: absolute;
    left: 50%; top: 50%;
    transform: translate(-50%, -50%);
    font-size: 40px;
  }
  .card--front .wordmark__dot { width: 96px; height: 96px; }

  .card--back .wordmark {
    position: absolute;
    left: 36px; top: 170px;
    font-size: 23px;
    gap: 12px;
    letter-spacing: 1.5px;
  }
  .card--back .wordmark__dot { width: 58px; height: 58px; }

  .divider {
    position: absolute;
    left: 430px; top: 95px;
    width: 2px; height: 240px;
    background: var(--rule);
  }
  .contact {
    position: absolute;
    left: 458px; top: 100px;
  }
  .contact__name {
    color: var(--blue);
    font-weight: 900;
    font-size: 30px;
    line-height: 1;
  }
  .contact__title {
    font-weight: 500;
    font-size: 16px;
    margin-top: 2px;
  }
  .contact__address {
    font-weight: 500;
    font-size: 17px;
    line-height: 1.25;
    margin-top: 14px;
  }
  .contact__list { list-style: none; margin-top: 10px; }
  .contact__item {
    display: flex;
    align-items: center;
    gap: 10px;
    font-weight: 500;
    font-size: 17px;
    line-height: 1.5;
  }
  .contact__icon { width: 16px; height: 16px; flex: none; }

  .band {
    position: absolute;
    left: 0; bottom: 0;
    width: 100%; height: 30px;
    background: var(--orange);
  }
</style>
</head>
<body>

<section class="card card--front" aria-label="Business card front">
  <div class="wordmark">
    <span class="wordmark__dot"></span>
    <span class="wordmark__name">Vantage Psychology</span>
  </div>
</section>

<section class="card card--back" aria-label="Business card back">
  <div class="wordmark">
    <span class="wordmark__dot"></span>
    <span class="wordmark__name">Vantage Psychology</span>
  </div>

  <div class="divider"></div>

  <div class="contact">
    <p class="contact__name">Elena Marsh</p>
    <p class="contact__title">Director</p>
    <p class="contact__address">The Marwick Block - 6127-48St.<br>Box 2716 Halvern, NB<br>T2K 3M8</p>
    <ul class="contact__list">
      <li class="contact__item">
        <svg class="contact__icon" viewBox="0 0 16 16" aria-hidden="true"><path d="M4 1.5l2.2 3-1.4 1.6c.9 2 2.3 3.5 4.3 4.4l1.6-1.4 3 2.2-1.2 2.4C7.8 13.6 2.4 8.2 1.6 2.7z" fill="none" stroke="#f6a05a" stroke-width="1.4" stroke-linejoin="round"/></svg>
        <span>403.555.0148 (VANT)</span>
      </li>
      <li class="contact__item">
        <svg class="contact__icon" viewBox="0 0 16 16" aria-hidden="true"><rect x="4" y="1.5" width="8" height="4" fill="none" stroke="#f6a05a" stroke-width="1.4"/><rect x="1.5" y="5.5" width="13" height="6" rx="1" fill="#f6a05a"/><rect x="4" y="9.5" width="8" height="5" fill="#fff" stroke="#f6a05a" stroke-width="1.4"/></svg>
        <span>403.555.0172</span>
      </li>
      <li class="contact__item">
        <svg class="contact__icon" viewBox="0 0 16 16" aria-hidden="true"><g fill="none" stroke="#f6a05a" stroke-width="1.2"><circle cx="8" cy="8" r="6.5"/><ellipse cx="8" cy="8" rx="3" ry="6.5"/><path d="M1.5 8h13M2.5 4.8h11M2.5 11.2h11"/></g></svg>
        <span>www.vantagepsychology-example.ca</span>
      </li>
    </ul>
  </div>

  <div class="band"></div>
</section>

</body>
</html>
```